Ashcombe Vista Business Cards

We need business card designs for a modern home development, Ashcombe Vista. We would like to see modern looking designs- clean and simple but striking. I've attached some images of one of the homes so you can see the style of the homes we are putting on the market and perhaps they will inspire your design! I've also attached the logo- both horizontal and vertical. We need to use the logo on the card. I've also attached a sign that has a map of the development. If you can use that and still keep the card nice and clean, great. If not, it's not a problem to leave the map out completely.

```html
<!DOCTYPE html>
<html lang="en">
<head>
<meta charset="utf-8">
<title>Ashcombe Vista – Business Card</title>
<link href="https://fonts.googleapis.com/css2?family=Saira+Semi+Condensed:wght@400;600&display=swap" rel="stylesheet">
<style>
  :root{
    --page:#ecebe8;
    --frame-grey:#c9cbcc;
    --card-white:#ffffff;
    --teal:#1a8596;
    --teal-back:#17879a;
    --sky:#1fa6dc;
    --charcoal:#3a3b3e;
    --ink:#2f3133;
    --muted:#5b5e61;
  }
  *{box-sizing:border-box;margin:0;padding:0}
  html,body{width:1057px;height:1200px;overflow:hidden}
  body{background:var(--page);font-family:"Saira Semi Condensed",Arial,sans-serif;position:relative}

  .card{position:absolute;top:240px;width:420px;height:720px;box-shadow:0 14px 30px rgba(0,0,0,.18)}

  /* front */
  .card--front{left:70px;background:var(--frame-grey);padding:16px}
  .front-face{position:relative;width:100%;height:100%;background:var(--card-white);overflow:hidden}
  .brand{position:absolute;left:38px;top:52px;display:flex;align-items:center;gap:12px}
  .brand-square{width:40px;height:40px;background:var(--teal)}
  .brand-name{font-weight:600;font-size:22px;letter-spacing:1px;color:var(--teal)}
  .person{position:absolute;left:38px;top:170px}
  .person-name{font-weight:400;font-size:40px;letter-spacing:1px;color:var(--ink);line-height:1}
  .person-role{margin-top:6px;font-size:15px;letter-spacing:2px;color:var(--muted)}

  .contact-band{position:absolute;left:0;right:0;top:272px;bottom:66px;background:var(--teal);
    clip-path:polygon(0 0,100% 16%,100% 100%,0 100%);padding:62px 0 0 38px}
  .contact-list{list-style:none}
  .contact-item{display:flex;align-items:center;gap:14px;margin-bottom:18px;color:var(--card-white);font-size:16px;letter-spacing:.5px}
  .contact-icon{width:26px;height:26px;flex:none}

  .address-bar{position:absolute;left:0;right:0;bottom:0;height:66px;background:var(--charcoal);
    display:flex;align-items:center;gap:12px;padding-left:30px;color:var(--card-white);font-size:15px;letter-spacing:.5px}

  /* back */
  .card--back{left:567px;background:var(--sky);padding:20px}
  .back-face{width:100%;height:100%;background:var(--teal-back);display:flex;align-items:center;justify-content:center}
  .back-brand{width:190px;height:250px;background:var(--card-white);display:flex;flex-direction:column;align-items:center;justify-content:center;gap:18px}
  .back-brand .brand-square{width:70px;height:70px}
  .back-brand-name{font-weight:600;font-size:26px;letter-spacing:2px;color:var(--teal);text-align:center;line-height:1.15}
</style>
</head>
<body>

<section class="card card--front" aria-label="Business card front">
  <div class="front-face">
    <div class="brand">
      <span class="brand-square"></span>
      <span class="brand-name">ASHCOMBE VISTA</span>
    </div>

    <div class="person">
      <h1 class="person-name">DANIEL MARSH</h1>
      <p class="person-role">GENERAL MANAGER</p>
    </div>

    <div class="contact-band">
      <ul class="contact-list">
        <li class="contact-item">
          <svg class="contact-icon" viewBox="0 0 26 26"><rect width="26" height="26" rx="3" fill="#fff"/><path d="M8 7c1-1 2-1 3 0l1 2c.4.8 0 1.4-.6 2 .8 1.6 2 2.8 3.6 3.6.6-.6 1.2-1 2-.6l2 1c1 1 1 2 0 3-1.2 1.2-3 1.4-5 .2-2.8-1.6-5-3.8-6.6-6.6C6.6 10 6.8 8.2 8 7z" fill="#1a8596"/></svg>
          <span>014 552 7310</span>
        </li>
        <li class="contact-item">
          <svg class="contact-icon" viewBox="0 0 26 26"><rect width="26" height="26" rx="3" fill="#fff"/><rect x="9" y="5" width="8" height="16" rx="1.5" fill="none" stroke="#1a8596" stroke-width="1.8"/><circle cx="13" cy="18" r="1" fill="#1a8596"/></svg>
          <span>014 552 7311</span>
        </li>
        <li class="contact-item">
          <svg class="contact-icon" viewBox="0 0 26 26"><rect width="26" height="26" rx="3" fill="#fff"/><rect x="6" y="8" width="14" height="10" fill="none" stroke="#1a8596" stroke-width="1.8"/><path d="M6 8l7 6 7-6" fill="none" stroke="#1a8596" stroke-width="1.8"/></svg>
          <span>d.marsh@ashcombevista.com</span>
        </li>
        <li class="contact-item">
          <svg class="contact-icon" viewBox="0 0 26 26"><rect width="26" height="26" rx="3" fill="#fff"/><circle cx="13" cy="13" r="7" fill="none" stroke="#1a8596" stroke-width="1.6"/><ellipse cx="13" cy="13" rx="3" ry="7" fill="none" stroke="#1a8596" stroke-width="1.4"/><path d="M6 13h14" stroke="#1a8596" stroke-width="1.4"/></svg>
          <span>www.ashcombevista.com</span>
        </li>
      </ul>
    </div>

    <div class="address-bar">
      <svg class="contact-icon" viewBox="0 0 26 26"><rect width="26" height="26" rx="3" fill="#fff"/><path d="M13 5a5 5 0 0 0-5 5c0 4 5 11 5 11s5-7 5-11a5 5 0 0 0-5-5z" fill="#3a3b3e"/><circle cx="13" cy="10" r="1.8" fill="#fff"/></svg>
      <span>42 Larkfield Road, Building 3, North Vale</span>
    </div>
  </div>
</section>

<section class="card card--back" aria-label="Business card back">
  <div class="back-face">
    <div class="back-brand">
      <span class="brand-square"></span>
      <span class="back-brand-name">ASHCOMBE<br>VISTA</span>
    </div>
  </div>
</section>

</body>
</html>
```